I need new business cards designed

I would like to get some new designs on business cards. I will upload my logo for reference. The business cards that were designed for me a few months ago were too difficult for the print companies to work with. My company is Brivoldex.com LLC. It is an art company that sells painting and expression cards online.

```html
<!DOCTYPE html>
<html lang="en">
<head>
<meta charset="utf-8">
<title>Brivoldex.com — Business Card</title>
<link rel="stylesheet" href="https://fonts.googleapis.com/css2?family=Carlito:wght@400;700&display=swap">
<style>
  :root {
    --backdrop: #d0d0d0;
    --card-white: #ffffff;
    --navy: #2b3174;
    --ink-grey: #8a8a8a;
    --sky: #03a2dc;
    --green: #8dc63f;
    --orange: #f7901e;
    --red: #ec2824;
    --white: #ffffff;
  }
  * { margin: 0; padding: 0; box-sizing: border-box; }
  html, body {
    width: 1200px;
    height: 1000px;
    overflow: hidden;
    background: var(--backdrop);
    font-family: "Carlito", "Calibri", sans-serif;
  }
  .canvas {
    position: relative;
    width: 1200px;
    height: 1000px;
  }
  .card {
    position: absolute;
    left: 293px;
    width: 613px;
    height: 352px;
    overflow: hidden;
  }
  .card--front { top: 97px; }
  .card--back { top: 540px; background: var(--card-white); }

  .front-artwork {
    position: absolute;
    inset: 0;
    background: linear-gradient(115deg, var(--green) 0%, var(--navy) 35%, var(--navy) 55%, var(--red) 78%, var(--sky) 100%);
  }
  .front-brand {
    position: absolute;
    left: 0;
    right: 0;
    top: 120px;
    text-align: center;
    color: var(--white);
    text-shadow: 2px 2px 2px rgba(0, 0, 0, 0.55);
  }
  .front-brand__name {
    font-size: 66px;
    font-weight: 400;
    line-height: 1;
    letter-spacing: 0.5px;
  }
  .front-brand__tagline {
    font-size: 38px;
    font-weight: 400;
    line-height: 1;
    margin-top: 4px;
  }
  .sep { font-size: 0.55em; vertical-align: 0.25em; }

  .brand-lockup {
    position: absolute;
    left: 47px;
    top: 52px;
    display: flex;
    align-items: center;
    gap: 12px;
  }
  .brand-lockup__square {
    width: 42px;
    height: 57px;
    background: var(--navy);
  }
  .brand-lockup__name {
    font-size: 25px;
    color: var(--navy);
    line-height: 1;
  }
  .brand-lockup__tagline {
    font-size: 15px;
    color: var(--sky);
    line-height: 1;
    margin-top: 3px;
  }

  .person {
    position: absolute;
    left: 47px;
    top: 150px;
    color: var(--navy);
    line-height: 1;
  }
  .person__name { font-size: 23px; font-weight: 700; }
  .person__role { font-size: 22px; font-weight: 400; margin-top: 2px; }

  .contact {
    position: absolute;
    left: 47px;
    top: 216px;
    font-size: 15.5px;
    line-height: 20px;
    color: var(--ink-grey);
  }
  .contact__group + .contact__group { margin-top: 20px; }

  .social {
    position: absolute;
    right: 38px;
    top: 307px;
    display: flex;
    gap: 10px;
  }
</style>
</head>
<body>
<main class="canvas">
  <section class="card card--front">
    <div class="front-artwork" role="img" aria-label="Bold flat geometric colour-block artwork in green, navy, orange, sky blue and red"></div>
    <div class="front-brand">
      <p class="front-brand__name">Brivoldex.com</p>
      <p class="front-brand__tagline">Painting Well <span class="sep">•</span> Boldly <span class="sep">•</span> Brightly</p>
    </div>
  </section>

  <section class="card card--back">
    <div class="brand-lockup">
      <div class="brand-lockup__square"></div>
      <div>
        <p class="brand-lockup__name">Brivoldex.com</p>
        <p class="brand-lockup__tagline">Painting Well <span class="sep">•</span> Boldly <span class="sep">•</span> Brightly</p>
      </div>
    </div>

    <div class="person">
      <p class="person__name">Dorian Vale Ashcombe</p>
      <p class="person__role">managing member</p>
    </div>

    <div class="contact">
      <div class="contact__group">
        <p>street address</p>
        <p>city, state, zip</p>
      </div>
      <div class="contact__group">
        <p>phone number</p>
        <p>dorianashcombe@brivoldex.com</p>
        <p>brivoldex.com</p>
      </div>
    </div>

    <svg class="social" width="86" height="22" viewBox="0 0 86 22" aria-label="Social profiles">
      <circle cx="11" cy="11" r="10" fill="var(--navy)"/>
      <circle cx="43" cy="11" r="10" fill="var(--navy)"/>
      <circle cx="75" cy="11" r="10" fill="var(--navy)"/>
    </svg>
  </section>
</main>
</body>
</html>
```